Music Web page

We are the largest community of artists, bands, podcasters and creators of music. We need web pages design.

What we need:
1. Registration form page
- Full Name
- Username
- Email Address
- Password
- Captcha

2. Songs/Artists gallery page
- Cover
- Simple MP3 Player
- Share | Like | Comments

3. Contact us page
- Name
- Email
- Phone
- Message
- Captcha

Send me a registration form first, If it makes me "hands on the air" , then I will continue to work with you.

Artists

Colors
eb1f27

Requirements
Nice to have
• Dark / black color for background

```html
<!DOCTYPE html>
<html lang="en">
<head>
<meta charset="utf-8">
<title>Soundyard – Sample Form Page</title>
<link href="https://fonts.googleapis.com/css2?family=Lato:wght@400;700;900&display=swap" rel="stylesheet">
<style>
:root{
  --red:#eb1f27;
  --black:#000;
  --charcoal:#222;
  --topbar:#1c1c1c;
  --button:#3d3d3d;
  --maroon:#2b0303;
  --white:#fff;
  --muted:#ddd;
  --map:#2b2b2b;
}
*{box-sizing:border-box;margin:0;padding:0}
html,body{width:1200px;height:3504px;overflow:hidden;background:var(--black)}
body{font-family:"Lato",sans-serif;color:var(--white)}
.page{width:1200px;height:3504px;position:relative}

.topbar{height:27px;background:var(--topbar);display:flex;justify-content:flex-end;align-items:center;gap:9px;padding-right:126px}
.topbar .social-square{width:15px;height:15px;background:#ddd;border-radius:2px}

.nav{height:108px;background:var(--red);display:flex;align-items:center;justify-content:space-between;padding:0 126px}
.brand{font-weight:900;font-size:42px;color:var(--black);letter-spacing:-1px}
.nav-links{display:flex;gap:30px;list-style:none;font-weight:700;font-size:13px;text-transform:uppercase}
.nav-links li:last-child{color:var(--black);border-bottom:2px solid var(--black)}

.hero{height:390px;text-align:center;padding-top:55px}
.hero h1{font-weight:900;font-size:80px;line-height:1}
.hero p{font-size:32px;margin-top:8px}
.pill{display:inline-block;background:var(--button);color:var(--white);border-radius:40px;font-size:18px;box-shadow:0 3px 0 rgba(0,0,0,.45)}
.hero .pill{margin-top:40px;padding:20px 30px}

.form-band{height:555px;background:var(--red);display:flex;padding:75px 123px 0}
.reg-form{width:456px;text-align:center;font-size:13px}
.reg-form .field{display:block;width:100%;height:30px;background:var(--white);margin-top:10px;color:#888;text-align:left;padding:7px 9px;font-size:13px}
.captcha-label{margin-top:12px}
.captcha-box{width:60px;height:24px;background:#f1f1f1;border:1px solid #999;margin:8px auto 4px}
.send{display:inline-block;margin-top:20px;background:var(--button);border-radius:30px;padding:16px 24px;font-size:16px;box-shadow:0 3px 0 rgba(0,0,0,.45)}
.form-intro{flex:1;text-align:center;padding-left:40px;padding-top:55px}
.form-intro h2{font-weight:900;font-size:64px}
.form-intro p{font-size:17px;line-height:1.6;max-width:440px;margin:18px auto 0}
.form-intro .pill{margin-top:26px;padding:15px 26px;font-size:16px}

.music{height:540px;background:var(--charcoal);text-align:center;padding-top:72px}
.music h2{font-weight:900;font-size:76px}
.features{display:flex;justify-content:center;gap:84px;margin-top:36px}
.feature{width:252px}
.feature .icon{width:162px;height:162px;border-radius:50%;margin:0 auto}
.feature h3{font-weight:900;font-size:20px;margin-top:30px}
.feature p{font-size:13px;line-height:1.5;margin-top:12px;color:var(--muted)}

.specialisation{height:498px;display:flex;align-items:center;padding-left:160px}
.spec-text{width:300px;text-align:center}
.spec-text h2{font-weight:900;font-size:68px;line-height:1.1;color:var(--red)}
.spec-text p{font-size:16px;margin-top:20px}
.donut{margin-left:190px}

.contact{height:456px;background:var(--maroon);display:flex;padding:36px 0 0 120px}
.contact-text{width:470px;text-align:center}
.contact-text h2{font-weight:900;font-size:66px}
.contact-text p{font-size:17px;line-height:1.65;margin-top:14px}
.contact-list{list-style:none;font-size:17px;line-height:1.65;margin-top:14px}
.contact-list svg{vertical-align:-3px;margin-right:6px}
.video{margin:78px 0 0 150px;width:456px;height:264px;border:9px solid var(--white);background:linear-gradient(135deg,#1a1a1a,#6d6d6d 50%,#111)}

.location{height:297px;text-align:center;padding-top:82px}
.location h2{font-weight:900;font-size:76px;line-height:1}
.location p{font-size:28px;margin-top:12px}

.map{height:378px;background:radial-gradient(ellipse at 80% 40%,#3a3a3a,var(--map) 60%)}

.footer{height:255px;background:var(--charcoal);text-align:center;padding-top:66px}
.footer-social{display:flex;justify-content:center;gap:18px}
.footer-social span{width:54px;height:54px;border-radius:50%;background:#444}
.footer-links{list-style:none;display:flex;justify-content:center;gap:12px;font-size:12px;margin-top:26px;text-transform:uppercase}
</style>
</head>
<body>
<div class="page">
  <div class="topbar">
    <span class="social-square"></span><span class="social-square"></span><span class="social-square"></span><span class="social-square"></span>
  </div>

  <header class="nav">
    <div class="brand">soundyard</div>
    <ul class="nav-links">
      <li>Home</li><li>Registration Form</li><li>Our Specialisation</li><li>Contact Us</li><li>Map</li>
    </ul>
  </header>

  <section class="hero">
    <h1>Sample Form Page</h1>
    <p>We look forward to your feedback.</p>
    <span class="pill">Scroll Down</span>
  </section>

  <section class="form-band">
    <div class="reg-form">
      <div>Registration Form</div>
      <span class="field">First Name</span>
      <span class="field">Last Name</span>
      <span class="field">Username</span>
      <span class="field">Email Address</span>
      <span class="field">Password</span>
      <div class="captcha-label">Answer this simple Captcha:</div>
      <div class="captcha-box"></div>
      <div>Your answer:</div>
      <span class="field"></span>
      <span class="send">Send</span>
    </div>
    <div class="form-intro">
      <h2>Your Form.</h2>
      <p>We thought it would be great if we could also showcase a little of our skills, scroll down to see what else we can do.</p>
      <span class="pill">
        <svg width="12" height="16" viewBox="0 0 12 16"><path d="M6 0a6 6 0 0 0-6 6c0 4.5 6 10 6 10s6-5.5 6-10a6 6 0 0 0-6-6zm0 8.5A2.5 2.5 0 1 1 6 3.5a2.5 2.5 0 0 1 0 5z" fill="#fff"/></svg>
        Learn More</span>
    </div>
  </section>

  <section class="music">
    <h2>Music is...</h2>
    <div class="features">
      <div class="feature">
        <div class="icon" role="img" aria-label="Flat globe illustration on a coral circle" style="background:radial-gradient(circle,#f0f0f0 0 38%,#e2574c 39%)"></div>
        <h3>Universal.</h3>
        <p>Lorem ipsum dolor sit amet, consectetuer adipiscing elit, sed diam nonummy nibh euismod.</p>
      </div>
      <div class="feature">
        <div class="icon" role="img" aria-label="Flat computer monitor illustration on a teal circle" style="background:radial-gradient(circle,#ececec 0 36%,#4cb6c0 37%)"></div>
        <h3>Digital.</h3>
        <p>Lorem ipsum dolor sit amet, consectetuer adipiscing elit, sed diam nonummy nibh euismod.</p>
      </div>
      <div class="feature">
        <div class="icon" role="img" aria-label="Flat red heart illustration on a yellow circle" style="background:radial-gradient(circle,#e24a4a 0 33%,#efb14a 34%)"></div>
        <h3>Love.</h3>
        <p>Lorem ipsum dolor sit amet, consectetuer adipiscing elit, sed diam nonummy nibh euismod.</p>
      </div>
    </div>
  </section>

  <section class="specialisation">
    <div class="spec-text">
      <h2>Our<br>Specialisation.</h2>
      <p>Roll over to see what the sections represents.</p>
    </div>
    <svg class="donut" width="380" height="380" viewBox="0 0 380 380" role="img" aria-label="Donut chart of specialisation areas">
      <g transform="rotate(-90 190 190)" fill="none" stroke-width="96">
        <circle cx="190" cy="190" r="138" stroke="#6e0508" stroke-dasharray="173 868"/>
        <circle cx="190" cy="190" r="138" stroke="#ff6b72" stroke-dasharray="130 868" stroke-dashoffset="-173"/>
        <circle cx="190" cy="190" r="138" stroke="#e83640" stroke-dasharray="182 868" stroke-dashoffset="-303"/>
        <circle cx="190" cy="190" r="138" stroke="#eb1f27" stroke-dasharray="130 868" stroke-dashoffset="-485"/>
        <circle cx="190" cy="190" r="138" stroke="#a3131a" stroke-dasharray="150 868" stroke-dashoffset="-615"/>
        <circle cx="190" cy="190" r="138" stroke="#7d0a0f" stroke-dasharray="103 868" stroke-dashoffset="-765"/>
      </g>
    </svg>
  </section>

  <section class="contact">
    <div class="contact-text">
      <h2>Contact Us.</h2>
      <p>Feel free to email us, phone us, smoke signal us, carrier pigeon us, or visit us. You can find us using our nifty map (just scroll down a bit).</p>
      <ul class="contact-list">
        <li><svg width="18" height="14" viewBox="0 0 18 14"><rect width="18" height="14" rx="1" fill="#fff"/><path d="M1 1l8 6 8-6" stroke="#2b0303" stroke-width="1.5" fill="none"/></svg>hello@soundyard.example</li>
        <li><svg width="14" height="16" viewBox="0 0 14 16"><path d="M3 0l3 4-2 2c1 2 2.5 3.5 4.5 4.5l2-2 3.5 3-2 4C6 15 0 9 0 2z" fill="#fff"/></svg>+65.5550.1234</li>
        <li><svg width="12" height="16" viewBox="0 0 12 16"><path d="M6 0a6 6 0 0 0-6 6c0 4.5 6 10 6 10s6-5.5 6-10a6 6 0 0 0-6-6zm0 8.5A2.5 2.5 0 1 1 6 3.5a2.5 2.5 0 0 1 0 5z" fill="#fff"/></svg>12 Harbour Lane, Unit 04-07,</li>
        <li>Quay Point, Singapore 000123</li>
      </ul>
    </div>
    <div class="video" role="img" aria-label="Embedded studio video with a smoky dark frame"></div>
  </section>

  <section class="location">
    <h2>Location.</h2>
    <p>Let’s meet up and discuss business-y things.</p>
  </section>

  <div class="map" role="img" aria-label="Dark street map of the studio area"></div>

  <footer class="footer">
    <div class="footer-social"><span></span><span></span><span></span><span></span></div>
    <ul class="footer-links">
      <li>Home</li><li>|</li><li>Registration Form</li><li>|</li><li>Our Specialisation</li><li>|</li><li>Contact Us</li><li>|</li><li>Map</li>
    </ul>
  </footer>
</div>
</body>
</html>
```